Illustration Design Project

I already upluaded the illustrator file. You can find the describtion of the product inside it. Text and the pucture of the product already designed.

This is a pharmacy product.

What I need is to add some colors and graphics to make this box attractive as much as possible. Even if you want to change the text and product's picture green color, it is OK.

Pharmacy

```html
<!DOCTYPE html>
<html lang="en">
<head>
<meta charset="utf-8">
<title>VELA Care – Electric Facial Cleanser Box</title>
<link rel="stylesheet" href="https://fonts.googleapis.com/css2?family=Noto+Serif:wght@700&family=Roboto:wght@400;700&display=swap">
<style>
  :root {
    --stage: #3a3a3a;
    --cream: #f7f2c9;
    --pattern-grey: #dcdad0;
    --sky: #a9dbe3;
    --peach: #f7c6b0;
    --teal: #1f8a96;
    --teal-dark: #1c6f78;
    --white: #ffffff;
  }
  * { margin: 0; padding: 0; box-sizing: border-box; }
  html, body { width: 1200px; height: 1184px; overflow: hidden; }
  body { background: var(--stage); position: relative; font-family: "Roboto", sans-serif; }

  .box-face {
    position: absolute; left: 100px; top: 42px; width: 1000px; height: 1100px;
    background: var(--sky); overflow: hidden;
  }

  /* decorative pattern areas rendered as soft flat fills */
  .pattern-band {
    position: absolute; left: 0; width: 100%;
    background: linear-gradient(180deg, var(--cream) 0%, var(--pattern-grey) 50%, var(--cream) 100%);
  }
  .pattern-band--top { top: 0; height: 110px; }
  .pattern-band--bottom { bottom: 0; height: 190px; }

  .brand-band { position: absolute; top: 110px; left: 0; width: 100%; height: 150px; }
  .brand-name {
    position: absolute; left: 120px; top: 42px;
    font-family: "Noto Serif", serif; font-weight: 700; font-size: 54px; color: var(--teal);
  }
  .brand-dot {
    position: absolute; right: -30px; top: 25px; width: 110px; height: 110px;
    border-radius: 50%; background: var(--teal);
  }

  .peach-panel { position: absolute; top: 290px; height: 430px; background: var(--peach); }
  .peach-panel__strip {
    position: absolute; left: 0; top: 0; width: 100%; height: 24px;
    background: linear-gradient(180deg, var(--cream), var(--pattern-grey));
  }
  .peach-panel--left { left: 60px; width: 340px; }
  .peach-panel--right { left: 640px; width: 300px; }

  .info-column {
    position: absolute; left: 400px; top: 290px; width: 240px;
    text-align: center; color: var(--white);
  }
  .model-code {
    display: inline-block; background: var(--teal-dark); color: var(--white);
    font-weight: 700; font-size: 26px; padding: 4px 14px; border-radius: 8px; letter-spacing: 1px;
  }
  .product-type { margin-top: 10px; color: var(--teal); }
  .product-type__main { font-size: 34px; font-weight: 700; letter-spacing: 3px; display: block; }
  .product-type__sub { font-size: 14px; letter-spacing: 2px; display: block; }
  .claim {
    margin-top: 34px; font-size: 15px; line-height: 1.5; letter-spacing: 1px; padding: 0 22px;
  }

  .product-visual {
    position: absolute; left: 40px; top: 540px; width: 290px; height: 560px;
    border-radius: 120px 40px 0 0;
    background: linear-gradient(165deg, rgba(255,255,255,0.75) 0%, rgba(220,240,243,0.7) 60%, rgba(127,188,196,0.6) 100%);
  }

  .water-badge { position: absolute; left: 470px; top: 680px; width: 200px; height: 240px; }
  .water-badge text { font-family: "Noto Serif", serif; font-weight: 700; fill: var(--white); }
</style>
</head>
<body>
  <main class="box-face">
    <div class="pattern-band pattern-band--top" role="img" aria-label="Repeating brand icon pattern band"></div>

    <header class="brand-band">
      <h1 class="brand-name">VELA Care</h1>
      <span class="brand-dot"></span>
    </header>

    <div class="peach-panel peach-panel--left">
      <div class="peach-panel__strip" role="img" aria-label="Repeating brand icon pattern strip"></div>
    </div>
    <div class="peach-panel peach-panel--right">
      <div class="peach-panel__strip" role="img" aria-label="Repeating brand icon pattern strip"></div>
    </div>

    <section class="info-column">
      <span class="model-code">VC-2041K</span>
      <h2 class="product-type">
        <span class="product-type__main">ELECTRIC</span>
        <span class="product-type__sub">FACIAL CLEANSER</span>
      </h2>
      <p class="claim">A PROFESSIONAL HOME USE TECHNOLOGY HELPING YOUR SKIN TO BREATH, REJUVENATE, REVIVE AND REVEALING GREATER YOUNGER LOOKING SKIN!</p>
    </section>

    <div class="pattern-band pattern-band--bottom" role="img" aria-label="Repeating brand icon pattern band"></div>

    <div class="product-visual" role="img" aria-label="Line illustration of the electric facial cleansing brush"></div>

    <svg class="water-badge" viewBox="0 0 200 240" aria-label="Water resistant IPX 6">
      <defs>
        <radialGradient id="drop-fill" cx="40%" cy="40%" r="70%">
          <stop offset="0%" stop-color="#4fb6c2"/>
          <stop offset="100%" stop-color="#176a74"/>
        </radialGradient>
      </defs>
      <path d="M150 0 C120 70 10 100 10 165 A90 75 0 0 0 190 165 C190 100 170 60 150 0 Z" fill="url(#drop-fill)"/>
      <g transform="rotate(-35 100 165)">
        <text x="100" y="140" text-anchor="middle" font-size="24">WATER</text>
        <text x="100" y="170" text-anchor="middle" font-size="24">RESISTANT</text>
        <text x="100" y="198" text-anchor="middle" font-size="22">IPX 6</text>
      </g>
    </svg>
  </main>
</body>
</html>
```